A layout of a webpage for oil trade platform

I would like to have a desgin of one page webpage (with section scrollling dowin) that woulf present the new product i.e. oil trade platform for wholesale buyers and sellers.
Layout should consist of the sections similar to the given at: https://klinika.pewnywybor.pl/system-zarzadzania-wizytami
However oil industy require more colors and more photo stories than here for doctor.
I. I woul imagine at first below menu a slider with brueg information about the product and its advantages with "more" button next to the prict screen of our platform on different displays (PC and mobile).
II. Bellow the slider I would imagine icons correspoing to the advantages of that plaftorm:
1. Purchase/sale process automation 24/7
2. Access to the best deals
3. Electronic offerings and orderings
4. Transaction status monitoring
5. Data and transaction security
II A) (optional):
In near future we would like to prepare a short video presenation. Hence please prepare a place to display that element here.
At the moment alternatvily please prepare a How it works section that would explan the platform operating process
III. Next secion is about benefits for Oil Purchaser
It can be done either by icons of by text and corresponding grahip for while section.
Benefits:
- Access to cheaper oil
- Convenience of online orders
- Possibility to compare prices on the market
- Transaction history
- Order status monitoring
- Seccurity and transparency of purchase
IV. Next seciont is about benefits for Oil Seller
Benefits:
- New sale channel
- Attracting new clients
- More oil sold
- Transaction security
- Possibility to integrate with distribution infrastructure and logistits for more efficient automation.
V. Contact form
VI. Footer
I would need a layout that that will correspond to the very dynamic logo but I would expect also a clean form, smoth and modern. It has to be proffessional layout with more corporate character.
It can use a paralax features if needed.

```html
<!DOCTYPE html>
<html lang="en">
<head>
<meta charset="utf-8">
<title>Naftora – Oil Trade Platform</title>
<link rel="stylesheet" href="https://fonts.googleapis.com/css2?family=Roboto:wght@400;500;700;900&display=swap">
<style>
:root{
  --navy:#2e3160;
  --ink:#222;
  --hero-top:#fdc97c;
  --hero-bottom:#f4ad66;
  --band-grey:#ececec;
  --icon-orange:#f59a6c;
  --icon-ring:#f8e36a;
  --coral:#f86a68;
  --sand:#fcc88e;
  --brown:#a8876a;
  --seller-bg:#fdc795;
  --btn-top:#fcb46c;
  --btn-bottom:#f1893a;
  --contact:#c96262;
  --link-blue:#1f6fb5;
  --send:#f7c49a;
  --page:#d9d9d9;
}
*{margin:0;padding:0;box-sizing:border-box}
html,body{width:1200px;height:3278px;overflow:hidden;background:var(--page)}
body{font-family:"Roboto",Arial,sans-serif}
.page{position:relative;width:1200px;height:3278px;overflow:hidden}

/* hero */
.hero{position:absolute;left:0;top:0;width:1200px;height:567px;background:linear-gradient(var(--hero-top),var(--hero-bottom))}
.brand{position:absolute;left:22px;top:44px;display:flex;align-items:center;gap:12px;font-weight:700;font-size:30px;color:var(--navy);letter-spacing:1px}
.brand-dot{width:40px;height:40px;border-radius:50%;background:var(--navy)}
.hero-title{position:absolute;left:60px;top:158px;font-weight:900;font-size:45px;color:var(--navy);white-space:nowrap}
.hero-text{position:absolute;left:20px;top:256px;width:645px;text-align:center;font-weight:700;font-size:16px;line-height:30px;color:#3a3a6a;white-space:nowrap}
.btn-more{position:absolute;left:257px;top:490px;width:165px;height:50px;border-radius:4px;background:linear-gradient(#fafafa,#cfcfcf);box-shadow:0 2px 3px rgba(0,0,0,.25);font-size:24px;color:var(--navy);display:flex;align-items:center;justify-content:center}
.hero-screens{position:absolute;left:680px;top:205px;width:520px;height:362px;background:linear-gradient(90deg,#1f2430 0%,#2f3a4e 40%,#eef0f3 41%,#f7f7f7 100%)}

/* features */
.features{position:absolute;left:0;top:567px;width:1200px;height:141px;background:var(--band-grey)}
.feature{position:absolute;top:14px;width:200px;text-align:center;font-size:17px;line-height:18px;color:var(--ink)}
.feature-icon{width:86px;height:86px;margin:0 auto 4px;border-radius:50%;background:var(--icon-orange);box-shadow:4px -2px 0 var(--icon-ring);display:flex;align-items:center;justify-content:center}

/* showcase */
.showcase{position:absolute;left:0;top:708px;width:1200px;height:426px;background:var(--coral)}
.showcase-title{position:absolute;left:95px;top:40px;font-weight:900;font-size:68px;color:var(--navy)}
.showcase-sub{position:absolute;left:45px;top:118px;font-weight:700;font-size:28px;color:var(--navy)}
.showcase-device{position:absolute;left:363px;top:8px;width:507px;height:409px;background:linear-gradient(#3a3a3a 0 75%,#d8d8d8 75%);border-radius:10px}

/* dashboard */
.dashboard{position:absolute;left:0;top:1134px;width:1200px;height:426px;background:var(--sand)}
.dashboard-shot{position:absolute;left:0;top:0;width:623px;height:426px;background:var(--brown)}
.dashboard-shot .screen{position:absolute;left:0;top:28px;width:608px;height:368px;background:linear-gradient(90deg,#2b3446 0 18%,#f1f3f7 18%)}
.dashboard-title{position:absolute;left:623px;top:14px;width:577px;text-align:center;font-weight:900;font-size:62px;color:var(--navy)}
.dashboard-sub{position:absolute;left:623px;top:96px;width:577px;text-align:center;font-weight:700;font-size:28px;color:var(--navy)}
.dashboard-text{position:absolute;left:630px;top:148px;width:550px;text-align:center;font-weight:700;font-size:15px;line-height:28px;color:var(--navy);white-space:nowrap}

/* buyer benefits */
.buyer{position:absolute;left:0;top:1560px;width:1200px;height:428px;background:#fff}
.buyer svg{position:absolute;left:0;top:0}
.b-txt{position:absolute;text-align:center;font-weight:900;color:#111;line-height:1;white-space:nowrap}
.buyer-banner{position:absolute;left:305px;top:186px;width:591px;height:50px;background:#fff;border-radius:4px;display:flex;align-items:center;justify-content:center;font-weight:900;font-size:34px;color:#111}

/* seller benefits */
.seller{position:absolute;left:0;top:1988px;width:1200px;height:420px;background:var(--seller-bg)}
.seller-figure{position:absolute;left:150px;top:0;width:310px;height:420px;background:linear-gradient(#f88f6a,#fbb080);border-radius:140px 140px 0 0}
.seller-btn{position:absolute;left:465px;width:703px;height:44px;border-radius:6px;background:linear-gradient(var(--btn-top),var(--btn-bottom));box-shadow:0 3px 0 rgba(200,100,40,.35);display:flex;align-items:center;justify-content:center;text-align:center;color:#fff;font-weight:700;font-size:26px;line-height:24px}
.seller-btn.small{font-size:20px;height:58px}

/* contact */
.contact{position:absolute;left:0;top:2408px;width:1200px;height:415px;background:var(--contact)}
.contact-icon{position:absolute;left:44px;top:25px}
.contact-head{position:absolute;left:232px;top:22px;width:820px;color:#fff;font-weight:700;font-size:27px;line-height:26px}
.contact-lead{position:absolute;left:232px;top:80px;color:var(--link-blue);font-weight:700;font-size:20px}
.field-label{position:absolute;color:#fff;font-weight:700;font-size:16px}
.field{position:absolute;width:290px;height:28px;background:#fff;border-radius:5px}
.field.wide{width:671px}
.btn-send{position:absolute;left:1015px;top:225px;width:113px;height:28px;border-radius:8px;background:var(--send);color:#fff;font-weight:700;font-size:16px;display:flex;align-items:center;justify-content:center}
</style>
</head>
<body>
<div class="page">

  <section class="hero">
    <div class="brand"><span class="brand-dot"></span>NAFTORA</div>
    <h1 class="hero-title">TITLE (Insert Your Texture)</h1>
    <p class="hero-text">I’m a paragrap.Click here to add your own text and edit me.It;s easy.Just click<br>“Edit&nbsp; Text” or double click me to add your own content and make changes<br>the font.Feel free to drag and drop me anywhere you like on your page.I’m a<br>great place for you to tell a story and let your users know alittle more about<br>you.This is a great space to write long text about your company and your<br>services.You can use this space to go into a little more detail about your<br>company.Talk about your team and services you provide.</p>
    <div class="btn-more">MORE</div>
    <div class="hero-screens" role="img" aria-label="Platform purchase list shown on a desktop and a mobile screen"></div>
  </section>

  <section class="features">
    <div class="feature" style="left:161px">
      <div class="feature-icon"><svg width="50" height="50" viewBox="0 0 52 52" fill="#fff"><rect x="6" y="10" width="40" height="36" rx="3"/><rect x="14" y="4" width="5" height="12" rx="2"/><rect x="33" y="4" width="5" height="12" rx="2"/><g fill="#f59a6c"><rect x="11" y="22" width="7" height="6"/><rect x="22" y="22" width="7" height="6"/><rect x="33" y="22" width="7" height="6"/><rect x="11" y="32" width="7" height="6"/><rect x="22" y="32" width="7" height="6"/><rect x="33" y="32" width="7" height="6"/></g></svg></div>
      Purchase/sale process<br>automation 24/7</div>
    <div class="feature" style="left:320px">
      <div class="feature-icon"><svg width="54" height="54" viewBox="0 0 56 56" fill="none" stroke="#fff" stroke-width="4"><circle cx="28" cy="28" r="24"/><path d="M20 16c-4 4 0 14 6 20s14 8 16 4l-5-5-4 3c-4-2-8-6-10-10l3-4z" fill="#fff" stroke="none"/></svg></div>
      Access to<br>the best deals</div>
    <div class="feature" style="left:496px">
      <div class="feature-icon"><svg width="38" height="58" viewBox="0 0 40 60"><rect x="4" y="2" width="32" height="56" rx="5" fill="#fff"/><rect x="8" y="9" width="24" height="40" fill="#f59a6c"/><circle cx="20" cy="53" r="2.5" fill="#f59a6c"/></svg></div>
      Electronic offerings<br>and orderings</div>
    <div class="feature" style="left:667px">
      <div class="feature-icon"><svg width="54" height="48" viewBox="0 0 56 50" fill="#fff"><path d="M4 17h10l14-12v40L14 33H4z"/><path d="M34 15q6 10 0 20M40 9q11 16 0 32M46 4q15 21 0 42" fill="none" stroke="#fff" stroke-width="4"/></svg></div>
      Transaction<br>status monitoring</div>
    <div class="feature" style="left:841px">
      <div class="feature-icon"><svg width="46" height="54" viewBox="0 0 48 56" fill="#fff"><path d="M12 24V16a12 12 0 0 1 24 0v8" fill="none" stroke="#fff" stroke-width="6"/><rect x="4" y="24" width="40" height="30" rx="4"/><rect x="21" y="33" width="6" height="12" rx="3" fill="#f59a6c"/></svg></div>
      Data and<br>transaction security</div>
  </section>

  <section class="showcase">
    <h2 class="showcase-title">TITLE</h2>
    <p class="showcase-sub">(Insert Your Texture)</p>
    <div class="showcase-device" role="img" aria-label="Desktop monitor presenting the platform video"></div>
  </section>

  <section class="dashboard">
    <div class="dashboard-shot"><div class="screen" role="img" aria-label="Platform dashboard with sales chart and order table"></div></div>
    <h2 class="dashboard-title">TITLE</h2>
    <p class="dashboard-sub">(Insert Your Texture)</p>
    <p class="dashboard-text">I’m a paragrap.Click here to add your own text and edit me.It;s<br>easy.Just click<br>“Edit&nbsp; Text” or double click me to add your own content and make<br>changes the font.Feel free to drag and drop me anywhere you like on<br>your page.I’m a great place for you to tell a story and let your users<br>know alittle more about you.This is a great space to write long text<br>about your company and your services.You can use this space to go<br>into a little more detail about your company.Talk about your team<br>and services you provide.</p>
  </section>

  <section class="buyer">
    <svg width="1200" height="428" viewBox="0 0 1200 428" role="img" aria-label="Colour-tinted photo strips of an oil purchaser ordering online">
      <polygon points="0,0 210,0 95,428 0,428" fill="#a6e6c3"/>
      <polygon points="242,0 426,0 312,428 127,428" fill="#f5c9a6"/>
      <polygon points="452,0 636,0 522,428 344,428" fill="#e88c86"/>
      <polygon points="668,0 853,0 738,428 554,428" fill="#dcd67e"/>
      <polygon points="878,0 1075,0 980,428 764,428" fill="#ad86cc"/>
      <polygon points="1107,0 1200,0 1200,428 1005,428" fill="#f47ae4"/>
    </svg>
    <div class="b-txt" style="left:0;top:36px;width:178px;font-size:33px;line-height:30px">ACCESS<br>TO<br>CHEAPER<br>OIL</div>
    <div class="b-txt" style="left:430px;top:36px;width:186px;font-size:22px;line-height:30px">POSIBILITY<br>TO COMPARE<br>PRICES ON<br>THE MARKET</div>
    <div class="b-txt" style="left:866px;top:38px;width:180px;font-size:44px;line-height:38px">ODER<br>STATUS<br><span style="font-size:22px">MONITORING</span></div>
    <div class="buyer-banner">BENEFITS FOR OIL PURCHASER</div>
    <div class="b-txt" style="left:150px;top:270px;width:190px;font-size:23px;line-height:28px">CONVENIENCE<br>OF ONLINE<br><span style="font-size:42px;line-height:44px">ODERS</span></div>
    <div class="b-txt" style="left:580px;top:302px;width:186px;font-size:21px;line-height:28px">TRANSACTION<br><span style="font-size:34px">HISTORY</span></div>
    <div class="b-txt" style="left:1000px;top:268px;width:200px;font-size:25px;line-height:32px">SECURITY<br><span style="font-size:42px;line-height:42px">AND</span><br><span style="font-size:22px">TRANSPARENCY</span><br>OF PURCHASE</div>
  </section>

  <section class="seller">
    <div class="seller-figure" role="img" aria-label="Illustration of a woman with shopping bags"></div>
    <div class="seller-btn" style="top:35px">NEW SALL CHANNEL</div>
    <div class="seller-btn" style="top:113px">ATTRACTING NEW CLIENTS</div>
    <div class="seller-btn" style="top:192px">MORE OILD SOLD</div>
    <div class="seller-btn" style="top:270px">TRANSACTION SECURITY</div>
    <div class="seller-btn small" style="top:342px">POSSIBILITY TO INTEGRATE WITH DISTRIBUTION<br>INFRASTRUCTURE AND IGOISTITS FOR MORE EFFICIENT AUTOMATIC</div>
  </section>

  <section class="contact">
    <svg class="contact-icon" width="166" height="124" viewBox="0 0 166 124"><rect x="2" y="2" width="162" height="120" rx="6" fill="#3a2a2a" stroke="#241818" stroke-width="3"/><path d="M6 8l77 62 77-62M10 116l52-44M156 116l-52-44" fill="none" stroke="#c96262" stroke-width="5"/></svg>
    <h2 class="contact-head">Have additional questions? Want to learn more?Talk to our consultant.</h2>
    <p class="contact-lead">Leave your details and we will contact you within 24 hours.</p>
    <span class="field-label" style="left:257px;top:124px">First Name</span>
    <span class="field-label" style="left:638px;top:124px">Last Name</span>
    <div class="field" style="left:257px;top:148px"></div>
    <div class="field" style="left:638px;top:148px"></div>
    <span class="field-label" style="left:257px;top:200px">Email</span>
    <span class="field-label" style="left:638px;top:201px">Telephone</span>
    <div class="field" style="left:256px;top:224px"></div>
    <div class="field" style="left:638px;top:224px"></div>
    <div class="btn-send">SEND</div>
    <span class="field-label" style="left:257px;top:276px">When can we contact you?</span>
    <div class="field wide" style="left:256px;top:298px"></div>
  </section>

</div>
</body>
</html>
```